TALRENO Business Cards

We require a business card for our company that provides IT consulting services. We already have a logo that needs to be used on the card. We want a clean professional looking design that incorporates our colours. Our main focus is providing managed services to business, which involves us looking after all of their IT requirements including managing servers/networks, projects, and procurement.

Industry/Entity Type

Information Technology

Requirements
Must have
• our logo, contact information, name, title, phone numbers

```html
<!DOCTYPE html>
<html lang="en">
<head>
<meta charset="utf-8">
<title>TALRENO Business Cards</title>
<link rel="stylesheet" href="https://fonts.googleapis.com/css2?family=Open+Sans:wght@400;600;700&display=swap">
<style>
  :root {
    --backdrop: #b3b3b4;
    --card-dark: #2e2d2e;
    --card-light: #f3f3f3;
    --brand-blue: #2398cf;
    --accent-gold: #e8b55a;
    --text-grey: #6b6b6b;
    --text-dark: #444444;
  }
  * { margin: 0; padding: 0; box-sizing: border-box; }
  html, body {
    width: 1200px; height: 1200px; overflow: hidden;
    background: var(--backdrop);
    font-family: "Open Sans", Arial, sans-serif;
  }
  .card { position: absolute; }
  .card-front {
    left: 322px; top: 261px; width: 552px; height: 316px;
    background: var(--card-dark);
  }
  .card-back {
    left: 332px; top: 662px; width: 534px; height: 304px;
    background: var(--card-light);
  }
  .wordmark {
    position: absolute;
    display: flex; align-items: center; gap: 12px;
    color: var(--brand-blue);
    font-weight: 600;
    letter-spacing: 3px;
    line-height: 1;
  }
  .wordmark-dot {
    border-radius: 50%;
    background: var(--brand-blue);
    flex: none;
  }
  .card-front .wordmark { left: 110px; top: 134px; font-size: 50px; }
  .card-front .wordmark-dot { width: 46px; height: 46px; }
  .card-back .wordmark { left: 278px; top: 112px; font-size: 34px; gap: 9px; letter-spacing: 2px; }
  .card-back .wordmark-dot { width: 32px; height: 32px; }
  .rule {
    position: absolute; height: 8px; background: var(--brand-blue); top: 129px;
  }
  .rule-left { left: 0; width: 264px; }
  .rule-right { left: 507px; width: 27px; }
  .name-block {
    position: absolute; left: 32px; top: 21px;
    border-left: 9px solid var(--accent-gold);
    padding-left: 8px; height: 56px;
  }
  .person-name {
    color: var(--brand-blue); font-weight: 700; font-size: 26px; line-height: 30px;
  }
  .person-title {
    color: var(--text-grey); font-size: 15px; line-height: 20px;
  }
  .contact-list {
    position: absolute; left: 32px; top: 192px; list-style: none;
    font-size: 12px; color: var(--text-dark);
  }
  .contact-list li { display: flex; align-items: flex-start; gap: 10px; line-height: 18px; margin-bottom: 1px; }
  .contact-list svg { width: 12px; height: 12px; margin-top: 3px; flex: none; fill: var(--brand-blue); }
</style>
</head>
<body>
  <section class="card card-front">
    <div class="wordmark"><span class="wordmark-dot"></span>TALRENO</div>
  </section>

  <section class="card card-back">
    <div class="name-block">
      <div class="person-name">MARA LINDQVIST</div>
      <div class="person-title">Business Development Manager</div>
    </div>
    <div class="rule rule-left"></div>
    <div class="wordmark"><span class="wordmark-dot"></span>TALRENO</div>
    <div class="rule rule-right"></div>
    <ul class="contact-list">
      <li>
        <svg viewBox="0 0 12 12" aria-hidden="true"><path d="M6 0a4.3 4.3 0 0 0-4.3 4.3C1.7 7.5 6 12 6 12s4.3-4.5 4.3-7.7A4.3 4.3 0 0 0 6 0zm0 6a1.7 1.7 0 1 1 0-3.4A1.7 1.7 0 0 1 6 6z"/></svg>
        <span>48 Cedar Lane<br>Box 2710, Pine Ridge, AB</span>
      </li>
      <li>
        <svg viewBox="0 0 12 12" aria-hidden="true"><path d="M2.4 0.5l2 2.3-1 1.4a7 7 0 0 0 4.4 4.4l1.4-1 2.3 2-1.2 1.9C5.6 11.2.8 6.4.5 1.7z"/></svg>
        <span>+403-555-0182</span>
      </li>
      <li>
        <svg viewBox="0 0 12 12" aria-hidden="true"><path d="M0 2h12v1.2L6 7 0 3.2zM0 4.6l6 3.8 6-3.8V10H0z"/></svg>
        <span>info@talreno.com</span>
      </li>
      <li>
        <svg viewBox="0 0 12 12" aria-hidden="true"><path d="M6 0a6 6 0 1 0 0 12A6 6 0 0 0 6 0zm0 1.2c.8 0 1.6 1.5 1.8 3.9H4.2C4.4 2.7 5.2 1.2 6 1.2zM4.2 6.3h3.6C7.6 8.6 6.8 10.8 6 10.8S4.4 8.6 4.2 6.3zM1.2 5.1a4.8 4.8 0 0 1 2.2-3.3A8 8 0 0 0 3 5.1zm0 1.2H3a8 8 0 0 0 .4 3.9 4.8 4.8 0 0 1-2.2-3.9zM9 5.1a8 8 0 0 0-.4-3.3 4.8 4.8 0 0 1 2.2 3.3zm0 1.2h1.8a4.8 4.8 0 0 1-2.2 3.9A8 8 0 0 0 9 6.3z"/></svg>
        <span>www.talreno.com</span>
      </li>
    </ul>
  </section>
</body>
</html>
```